Harbourline Green Jack Socials - Flyer

So now that i have the logo, I need a flyer made up for printing to be delivered to businesses and residential homes.
Below is some information that I want included in the design, in any order and in anyway.
What better way to spend time with family, friends or workmates then to enjoy 2 hours of barefoot bowls.
We can cater for Xmas Parties, Buck's and Hen's Parties, Birthday Parties, Team Building events.
We have food and drink packages to suit all your needs.
So why not come along and have the best fun you can have on 2 feet!
We have 2 locations at Wendlebrook Sports and Bowling Club and Mossvale Ridge Bowling Club
Prices start from $12pp for 2 hours of lawn bowls fun
Contact Colin Parrow on 0478 615 240 or visit our website www.greenjacksocials-example.com.au for more information and to enquire about your function today!

```html
<!DOCTYPE html>
<html lang="en">
<head>
<meta charset="utf-8">
<title>Harbourline Green Jack Socials – Flyer</title>
<link rel="stylesheet" href="https://fonts.googleapis.com/css2?family=Kurale&family=Arimo:wght@400;700&family=Open+Sans:ital,wght@0,400;0,700;1,700&display=swap">
<style>
  :root {
    --page: #ffffff;
    --navy: #07496f;
    --ink: #0a4a72;
    --white: #ffffff;
    --peach: #f5c29c;
    --mint: #b6dbb0;
    --ball: #0c3c5c;
    --rule: #1b1b1b;
  }
  html, body { margin: 0; padding: 0; overflow: hidden; background: var(--page); }
  .canvas { position: relative; width: 1200px; height: 900px; overflow: hidden; background: var(--page); }
  .flyer { position: absolute; left: 278px; top: 0; width: 640px; height: 900px; border-left: 1px solid var(--rule); border-right: 1px solid var(--rule); box-sizing: border-box; }
  .flyer__header { position: absolute; left: 0; top: 0; width: 100%; height: 97px; background: var(--white); border-bottom: 1px solid var(--rule); }
  .flyer__body { position: absolute; left: 0; top: 97px; width: 100%; height: 803px; background: var(--navy); }
  .shapes { position: absolute; left: 0; top: 0; width: 1200px; height: 900px; }
  .t { position: absolute; white-space: nowrap; margin: 0; line-height: 1; }
  .c { transform: translateX(-50%); text-align: center; }
  .headline { font-family: "Kurale", serif; color: var(--ink); font-size: 27px; }
  .invite { font-family: "Arimo", Arial, sans-serif; color: var(--white); }
  .pitch { font-family: "Open Sans", sans-serif; color: var(--ink); font-size: 19px; }
  .pitch--strong { font-weight: 700; }
  .count { display: inline-block; background: var(--ink); color: var(--white); font-size: 15px; padding: 2px 6px; }
  .venue { font-family: "Open Sans", sans-serif; font-style: italic; font-weight: 700; color: var(--ink); font-size: 15.5px; line-height: 22px; text-align: center; }
  .details { font-family: "Open Sans", sans-serif; color: var(--white); font-size: 9px; line-height: 12px; }
  .price { font-family: "Open Sans", sans-serif; color: var(--white); font-size: 10px; }
  .brand-box { position: absolute; left: 555px; top: 809px; width: 83px; height: 42px; border: 1px solid var(--white); box-sizing: border-box; display: flex; align-items: center; justify-content: center; font-family: "Arimo", Arial, sans-serif; color: var(--white); font-size: 13px; }
  .contact { font-family: "Arimo", Arial, sans-serif; color: var(--white); font-weight: 700; font-size: 14px; }
  .contact small { font-weight: 400; font-size: 11px; }
  .web { font-family: "Arimo", Arial, sans-serif; color: var(--white); font-weight: 700; font-size: 10.5px; }
</style>
</head>
<body>
<div class="canvas">
  <div class="flyer">
    <div class="flyer__header"></div>
    <div class="flyer__body"></div>
  </div>

  <svg class="shapes" viewBox="0 0 1200 900" aria-hidden="false">
    <g class="bowls" fill="var(--ball)">
      <circle cx="362" cy="131" r="13"/><circle cx="468" cy="226" r="13"/><circle cx="493" cy="254" r="13"/>
      <circle cx="318" cy="335" r="13"/><circle cx="328" cy="528" r="13"/><circle cx="385" cy="567" r="13"/>
      <circle cx="313" cy="719" r="13"/><circle cx="508" cy="780" r="13"/><circle cx="784" cy="142" r="13"/>
      <circle cx="866" cy="118" r="13"/><circle cx="823" cy="244" r="13"/><circle cx="858" cy="384" r="13"/>
      <circle cx="821" cy="545" r="13"/><circle cx="830" cy="786" r="13"/><circle cx="800" cy="840" r="13"/>
    </g>
    <path class="centre-disc" d="M455 420 C455 360 515 338 580 338 C645 338 705 360 705 420 L705 640 L455 640 Z" fill="var(--white)"/>
    <rect class="foot foot--left" role="img" aria-label="Peach silhouette of a bare left foot" x="343" y="305" width="197" height="363" rx="90" fill="var(--peach)"/>
    <rect class="foot foot--right" role="img" aria-label="Green silhouette of a bare right foot" x="620" y="308" width="195" height="360" rx="90" fill="var(--mint)"/>
    <g class="pointers" stroke="var(--ink)" stroke-width="1.3" fill="var(--ink)">
      <line x1="530" y1="612" x2="480" y2="563"/><path d="M475 558 L485 562 L480 567 Z"/>
      <line x1="622" y1="612" x2="678" y2="563"/><path d="M683 558 L673 562 L678 567 Z"/>
    </g>
  </svg>

  <p class="t headline" style="left:346px; top:18px;">Looking for a better way to spend time</p>
  <p class="t headline" style="left:481px; top:51px;">with family, friends or workmates?</p>

  <p class="t invite c" style="left:580px; top:162px; font-size:28px;">Why not</p>
  <p class="t invite c" style="left:580px; top:188px; font-size:19px;">come along</p>
  <p class="t invite c" style="left:580px; top:211px; font-size:13px;">amidst nature and</p>
  <p class="t invite c" style="left:580px; top:228px; font-size:16px;">experience the</p>
  <p class="t invite c" style="left:580px; top:245px; font-size:17px;">best fun you</p>
  <p class="t invite c" style="left:580px; top:264px; font-size:17px;">can have on</p>
  <p class="t invite c" style="left:580px; top:283px; font-size:38px;">2 feet</p>

  <p class="t pitch pitch--strong c" style="left:575px; top:348px;">Lawn</p>
  <p class="t pitch pitch--strong c" style="left:575px; top:371px;">Bowls</p>
  <p class="t pitch pitch--strong c" style="left:575px; top:394px;">Party,</p>
  <p class="t pitch c" style="left:575px; top:416px;">the</p>
  <p class="t pitch c" style="left:575px; top:439px;">unique</p>
  <p class="t pitch c" style="left:575px; top:461px;">choice</p>
  <p class="t pitch c" style="left:575px; top:484px;">you can</p>
  <p class="t pitch c" style="left:575px; top:507px;">ever make!</p>
  <p class="t pitch c" style="left:575px; top:531px;">We have</p>
  <p class="t pitch c" style="left:577px; top:555px;"><span class="count">2</span></p>
  <p class="t pitch c" style="left:577px; top:577px;">good</p>
  <p class="t pitch c" style="left:577px; top:599px;">locations</p>

  <p class="t venue c" style="left:463px; top:483px;">Wendlebrook<br>Sports and<br>Bowling Club</p>
  <p class="t venue c" style="left:696px; top:508px;">Mossvale Ridge<br>Bowling Club</p>

  <p class="t details c" style="left:605px; top:690px;">We cater for Xmas Parties, Buck's and Hen's Parties, Birthday Parties, Team Building events.<br>We also have food and drink packages to suit all your needs.</p>
  <p class="t price c" style="left:605px; top:723px;">“Prices start from <strong>$12pp for 2 hours</strong> of lawn bowls fun”</p>

  <div class="brand-box">Logo</div>

  <p class="t contact c" style="left:595px; top:862px;">Contact: Colin Parrow on 0478 615 240 <small>or</small></p>
  <p class="t web c" style="left:594px; top:881px;">Visit our website www.greenjacksocials-example.com.au for more information and to enquire about your function today!</p>
</div>
</body>
</html>
```